Tidal Fern Business Cards

We need something new, fun and exciting for business cards. Our current ones are just plain and we need a design that pops. We want name, position held, phone, email on the front, and a 20% discount on the back. I have also uploaded our old business cards creative to see what we are not wanting, and how boring they were and we want something jazzed up from this, cool design and catches people attention.

```html
<!DOCTYPE html>
<html lang="en">
<head>
<meta charset="utf-8">
<title>Tidal Fern Business Cards</title>
<link href="https://fonts.googleapis.com/css2?family=Lato:ital,wght@0,400;0,700;0,900;1,400&display=swap" rel="stylesheet">
<style>
  :root {
    --navy: #173a6e;
    --navy-soft: #1e4580;
    --coral: #f26b6b;
    --white: #ffffff;
    --ink: #555a63;
    --rule: #4a4a4a;
    --backdrop: #e9e6e2;
  }
  * { box-sizing: border-box; margin: 0; padding: 0; }
  html, body { width: 1200px; height: 847px; overflow: hidden; }
  body {
    background: var(--backdrop);
    font-family: "Lato", sans-serif;
    position: relative;
  }
  .card {
    position: absolute;
    width: 540px;
    height: 309px;
    box-shadow: 0 6px 18px rgba(0,0,0,0.18);
    overflow: hidden;
  }
  /* Back of card */
  .card-back { left: 40px; top: 269px; background: var(--navy); }
  .back-pattern {
    position: absolute; inset: 0;
    background: linear-gradient(135deg, var(--navy) 0%, var(--navy-soft) 50%, var(--navy) 100%);
  }
  .brand {
    position: absolute;
    display: flex; align-items: center; gap: 12px;
    font-weight: 700;
    letter-spacing: 0.5px;
    white-space: nowrap;
  }
  .brand-dot { width: 34px; height: 34px; border-radius: 50%; background: var(--coral); flex: none; }
  .card-back .brand { left: 112px; top: 110px; font-size: 52px; color: var(--white); }
  .discount {
    position: absolute; left: 0; right: 0; top: 230px;
    display: flex; align-items: center; gap: 14px;
    padding: 0 0 0 0;
  }
  .discount-rule { height: 1px; background: var(--coral); }
  .discount-rule.left { width: 150px; }
  .discount-rule.right { flex: 1; }
  .discount-text { color: var(--coral); font-size: 22px; }

  /* Front of card */
  .card-front { left: 620px; top: 269px; background: var(--white); }
  .card-front .brand { right: 30px; top: 42px; font-size: 44px; color: var(--navy); }
  .person { position: absolute; left: 30px; top: 56px; }
  .person-name { font-weight: 900; font-size: 24px; color: var(--navy); letter-spacing: 0.5px; }
  .person-role { font-size: 14px; color: var(--ink); margin-top: 0; }
  .divider { position: absolute; left: 30px; right: 30px; top: 128px; height: 1px; background: var(--rule); }
  .contacts { position: absolute; left: 30px; top: 142px; list-style: none; }
  .contacts li { display: flex; align-items: center; gap: 10px; font-size: 15px; color: var(--ink); line-height: 24px; }
  .contacts svg { width: 14px; height: 14px; fill: var(--navy); }
  .address { position: absolute; right: 30px; top: 210px; text-align: right; font-size: 15px; color: var(--ink); line-height: 21px; }
  .address-rule { position: absolute; right: 30px; width: 230px; top: 204px; height: 1px; background: var(--rule); }
  .footer-band { position: absolute; left: 0; right: 0; bottom: 0; height: 30px; }
  .footer-band svg { display: block; width: 100%; height: 100%; }
  .web { position: absolute; right: 30px; bottom: 6px; color: var(--white); font-size: 15px; letter-spacing: 0.3px; }
</style>
</head>
<body>
  <section class="card card-back" aria-label="Card back">
    <div class="back-pattern" role="img" aria-label="Repeating brand-symbol pattern in muted navy"></div>
    <div class="brand"><span class="brand-dot"></span>Tidal Fern</div>
    <div class="discount">
      <span class="discount-rule left"></span>
      <span class="discount-text">20% discount</span>
      <span class="discount-rule right"></span>
    </div>
  </section>

  <section class="card card-front" aria-label="Card front">
    <div class="brand"><span class="brand-dot"></span>Tidal Fern</div>
    <div class="person">
      <p class="person-name">MARA QUINN</p>
      <p class="person-role">CFO</p>
    </div>
    <div class="divider"></div>
    <ul class="contacts">
      <li><svg viewBox="0 0 24 24"><path d="M6.6 10.8a15.1 15.1 0 0 0 6.6 6.6l2.2-2.2a1 1 0 0 1 1-.25 11.4 11.4 0 0 0 3.6.57 1 1 0 0 1 1 1V20a1 1 0 0 1-1 1A17 17 0 0 1 3 4a1 1 0 0 1 1-1h3.5a1 1 0 0 1 1 1c0 1.25.2 2.45.57 3.57a1 1 0 0 1-.25 1z"/></svg>5550142876</li>
      <li><svg viewBox="0 0 24 24"><path d="M2 5h20v14H2z M2 5l10 8 10-8" /></svg>hello@tidalfern.com</li>
    </ul>
    <div class="address-rule"></div>
    <p class="address">1234 First Line Address<br>5678 Second Line Address</p>
    <div class="footer-band">
      <svg viewBox="0 0 540 30" preserveAspectRatio="none">
        <rect x="0" y="14" width="260" height="16" fill="var(--coral)"/>
        <polygon points="230,30 260,6 540,6 540,30" fill="var(--navy)"/>
      </svg>
    </div>
    <p class="web">www.tidalfern.com</p>
  </section>
</body>
</html>
```